Quillmoor Farm Organic Flower Farm, Farmer Florist

I am a flower grower and florist, so I do everything from the field to the vase. I want to include my website, phone, email and instagram

```html
<!DOCTYPE html>
<html lang="en">
<head>
<meta charset="utf-8">
<title>Quillmoor Farm – Business Cards</title>
<link rel="stylesheet" href="https://fonts.googleapis.com/css2?family=Cinzel:wght@400;600&family=Arimo:wght@400&display=swap">
<style>
  :root {
    --backdrop: #0c0c0c;
    --card: #050505;
    --rose: #e8898a;
    --rose-muted: #7c3c42;
    --rose-dim: #4a2428;
    --rule: #2a1d1f;
    --emboss-light: #151515;
    --emboss-dark: #0a0a0a;
  }
  * { margin: 0; padding: 0; box-sizing: border-box; }
  html, body { width: 1200px; height: 820px; overflow: hidden; background: var(--backdrop); }
  .canvas { position: relative; width: 1200px; height: 820px; background: var(--backdrop); }

  .card {
    position: absolute;
    width: 560px; height: 320px;
    background: var(--card);
    border-radius: 3px;
  }
  .card--contact { left: 50px; top: 450px; }
  .card--brand { left: 600px; top: 60px; }

  /* contact side */
  .brand-block {
    position: absolute; right: 70px; top: 38px;
    text-align: center; width: 250px;
  }
  .brand-block__mark {
    width: 34px; height: 34px; margin: 0 auto 10px;
    background: var(--rose);
  }
  .brand-name {
    font-family: "Cinzel", serif; font-weight: 400;
    font-size: 34px; letter-spacing: 3px; color: var(--rose-muted);
    line-height: 1;
  }
  .brand-tagline {
    font-family: "Cinzel", serif; font-weight: 400;
    font-size: 13px; letter-spacing: 2px; color: var(--rose-muted);
    margin-top: 8px;
  }
  .brand-est {
    font-family: "Cinzel", serif; font-size: 9px; letter-spacing: 4px;
    color: var(--rose-muted); margin-top: 5px;
  }
  .divider {
    position: absolute; left: 210px; right: 40px; top: 170px;
    height: 1px; background: var(--rule);
  }
  .person { position: absolute; left: 40px; top: 150px; }
  .person__name {
    font-family: "Cinzel", serif; font-weight: 600;
    font-size: 22px; letter-spacing: 1px; color: var(--rose);
  }
  .person__role {
    font-family: "Arimo", sans-serif; font-size: 15px; color: var(--rose-muted);
    margin-top: 2px;
  }
  .contact-list { position: absolute; left: 44px; top: 228px; list-style: none; }
  .contact-list li {
    display: flex; align-items: center; gap: 10px;
    font-family: "Arimo", sans-serif; font-size: 15px; color: var(--rose);
    height: 24px;
  }
  .contact-list svg { width: 16px; height: 16px; fill: none; stroke: var(--rose); stroke-width: 1.6; }
  .social-handle {
    position: absolute; right: 40px; top: 205px;
    display: flex; align-items: center; gap: 10px;
    font-family: "Arimo", sans-serif; font-size: 15px; color: var(--rose-muted);
  }
  .social-handle__dot {
    width: 16px; height: 16px; border: 1.6px solid var(--rose); border-radius: 50%;
  }

  /* brand side */
  .card--brand { box-shadow: 0 3px 0 #8a4a52, 0 6px 0 #6e3a40, 0 8px 0 #8a4a52; }
  .emboss-area {
    position: absolute; left: 60px; top: 40px; width: 240px; height: 280px;
    border-radius: 110px 110px 0 0;
    background: linear-gradient(160deg, var(--emboss-light), var(--emboss-dark));
  }
  .brand-side-text {
    position: absolute; right: 40px; top: 120px; text-align: right;
  }
  .brand-side-text .brand-name { font-size: 30px; }
  .brand-side-text .brand-tagline { text-align: right; }
</style>
</head>
<body>
<main class="canvas">

  <section class="card card--contact" aria-label="Business card, contact side">
    <div class="brand-block">
      <div class="brand-block__mark"></div>
      <div class="brand-name">QUILLMOOR</div>
      <div class="brand-tagline">organic flower farm</div>
      <div class="brand-est">EST. 2019</div>
    </div>
    <div class="divider"></div>

    <div class="person">
      <div class="person__name">ELLIS MARROW</div>
      <div class="person__role">Managing Director</div>
    </div>

    <ul class="contact-list">
      <li>
        <svg viewBox="0 0 16 16"><path d="M3 2l3 3-1.5 2a8 8 0 0 0 4.5 4.5L11 10l3 3-2 2C6 14 2 10 1 4z"/></svg>
        021-555 0147 62
      </li>
      <li>
        <svg viewBox="0 0 16 16"><rect x="1.5" y="3.5" width="13" height="9"/><path d="M1.5 3.5L8 9l6.5-5.5"/></svg>
        hello@quillmoor.com
      </li>
      <li>
        <svg viewBox="0 0 16 16"><circle cx="8" cy="8" r="6.5"/><ellipse cx="8" cy="8" rx="3" ry="6.5"/><path d="M1.5 8h13M2.5 5h11M2.5 11h11"/></svg>
        www.quillmoorfarm.com
      </li>
    </ul>

    <div class="social-handle">
      @quillmoorfarm
      <span class="social-handle__dot"></span>
    </div>
  </section>

  <section class="card card--brand" aria-label="Business card, brand side">
    <div class="emboss-area" role="img" aria-label="Blind-embossed farm emblem in black on black"></div>
    <div class="brand-side-text">
      <div class="brand-name">QUILLMOOR</div>
      <div class="brand-tagline">organic flower farm</div>
    </div>
  </section>

</main>
</body>
</html>
```